A property investment company, looking to provide lovely sustainable homes for familys and individua

For a small investment business i am starting which will buy and refurbish unloved houses and apartments to rent out or resell. the company name is my family surname (HARGREAVE). <br/>i would like the design to be simple with maybe some emphasis on an ethical and sustainable/environmentally friendly approach with a branding of maybe trees blended with some houses and or apartments.<br/>The colours i like for this design would be mainly green on either a white or black background.
Target Market(s)
This business card is to be used for professional people such as estate agents
mortgage brokers, solicitors and trades people.
Industry/Entity Type
Real Estate
Contact Information for Business Card
owner/director-Martin hargreave
e-mail-martin@hvholdings.co.uk
website-hargreavehomeholdings.co.uk
mobile-07700945318
landline-02079460581
Look and feel

```html
<!DOCTYPE html>
<html lang="en">
<head>
<meta charset="utf-8">
<title>Hargreave Property – Business Card</title>
<link href="https://fonts.googleapis.com/css2?family=Libre+Baskerville:wght@700&family=Marcellus&family=Poppins:wght@600&family=Questrial&display=swap" rel="stylesheet">
<style>
  :root {
    --teal: #33b8a3;
    --teal-faint: #9edcd0;
    --green: #8dc63f;
    --ink: #141414;
    --grey: #6a6a6a;
    --paper: #ffffff;
    --backdrop: #efefef;
  }
  * { margin: 0; padding: 0; box-sizing: border-box; }
  html, body { width: 1200px; height: 1200px; overflow: hidden; }
  body { background: var(--backdrop); position: relative; font-family: "Questrial", sans-serif; color: var(--ink); }

  .card {
    position: absolute; left: 247px; width: 706px; height: 404px;
    background: var(--paper); border-radius: 30px; overflow: hidden;
  }
  .card--front { top: 130px; }
  .card--back { top: 666px; }

  /* brand lockup */
  .brand { position: absolute; text-align: center; transform: translateX(-50%); }
  .brand__dot { display: block; margin: 0 auto; border-radius: 50%; background: var(--green); }
  .brand__name, .brand__sub {
    font-family: "Libre Baskerville", serif; font-weight: 700; color: var(--ink); line-height: 1;
  }
  .brand__sub { letter-spacing: 0.35em; margin-right: -0.35em; }

  .card--front .brand { left: 223px; top: 89px; }
  .card--front .brand__dot { width: 162px; height: 162px; margin-bottom: 22px; }
  .card--front .brand__name { font-size: 33px; }
  .card--front .brand__sub { font-size: 15px; margin-top: 10px; }

  .card--back .brand { left: 139px; top: 89px; }
  .card--back .brand__dot { width: 124px; height: 124px; margin-bottom: 16px; }
  .card--back .brand__name { font-size: 25px; }
  .card--back .brand__sub { font-size: 11px; margin-top: 7px; }

  /* teal side panel */
  .side-panel { position: absolute; left: 446px; top: 0; width: 260px; height: 100%; background: var(--teal); overflow: hidden; }
  .side-panel__word {
    position: absolute; left: 0; top: 36px; width: 44px; height: 330px;
    font-family: "Libre Baskerville", serif; font-weight: 700; font-size: 46px;
    color: var(--teal-faint); writing-mode: vertical-rl; line-height: 44px; white-space: nowrap;
    text-align: center;
  }
  .side-panel__ring {
    position: absolute; left: 97px; top: 38px; width: 330px; height: 330px;
    border-radius: 50%; border: 14px solid var(--teal-faint);
  }

  /* back details */
  .divider { position: absolute; left: 262px; top: 44px; width: 3px; height: 275px; background: var(--ink); }
  .person { position: absolute; left: 295px; top: 52px; }
  .person__name { font-family: "Marcellus", serif; font-size: 48px; line-height: 1; }
  .person__role { font-family: "Poppins", sans-serif; font-weight: 600; font-size: 22px; letter-spacing: 0.2em; color: var(--grey); margin-top: 8px; line-height: 1; }

  .contacts { position: absolute; left: 295px; top: 178px; list-style: none; }
  .contacts__item { display: flex; align-items: center; height: 33.5px; font-size: 21px; }
  .contacts__icon { width: 28px; height: 24px; margin-right: 17px; flex: none; }

  .base-band { position: absolute; left: 0; bottom: 0; width: 100%; height: 42px; background: var(--teal); }
</style>
</head>
<body>

<section class="card card--front">
  <div class="brand">
    <span class="brand__dot"></span>
    <div class="brand__name">HARGREAVE</div>
    <div class="brand__sub">PROPERTY</div>
  </div>
  <div class="side-panel">
    <div class="side-panel__word">HARGREAVE</div>
    <div class="side-panel__ring"></div>
  </div>
</section>

<section class="card card--back">
  <div class="brand">
    <span class="brand__dot"></span>
    <div class="brand__name">HARGREAVE</div>
    <div class="brand__sub">PROPERTY</div>
  </div>

  <div class="divider"></div>

  <div class="person">
    <div class="person__name">Martin Hargreave</div>
    <div class="person__role">DIRECTOR</div>
  </div>

  <ul class="contacts">
    <li class="contacts__item">
      <svg class="contacts__icon" viewBox="0 0 28 24" fill="none" stroke="#141414" stroke-width="2"><rect x="1" y="4" width="26" height="17"/><path d="M1 4l13 10 13-10M1 21l10-9M27 21l-10-9"/></svg>
      martin@hvholdings.co.uk
    </li>
    <li class="contacts__item">
      <svg class="contacts__icon" viewBox="0 0 28 24" fill="none" stroke="#141414" stroke-width="1.8"><circle cx="14" cy="12" r="11"/><ellipse cx="14" cy="12" rx="5" ry="11"/><path d="M3 12h22M5 6h18M5 18h18M14 1v22"/></svg>
      hargreavehomeholdings.co.uk
    </li>
    <li class="contacts__item">
      <svg class="contacts__icon" viewBox="0 0 28 24"><rect x="8" y="0" width="12" height="24" rx="2" fill="#141414"/><rect x="10" y="3" width="8" height="16" fill="#fff"/></svg>
      07700945318
    </li>
    <li class="contacts__item">
      <svg class="contacts__icon" viewBox="0 0 28 24" fill="none" stroke="#141414" stroke-width="1.8"><path d="M7 2l4 5-2 3c1 3 3 6 6 8l3-2 5 4-2 3c-9 0-17-9-17-18z"/></svg>
      02079460581
    </li>
  </ul>

  <div class="base-band"></div>
</section>

</body>
</html>
```